Etikett-Design für Olivenöl
Unsere Vorgaben wurden gut aufgenommen. Der erste Entwurf hat uns sofort angesprochen. Wir hatten noch ein paar Modifikationen und das Projekt war sehr schnell erfolgreich abgeschlossen. Wir werden weitere Themen hier beauftragen. Besten Dank.
Zielgruppe
Einzelhandel. Die Zielgruppe ist 30 bis 55 Jahre alt, weiblich sowie männlich.
Aufgabenstellung
Das Label für die 100ml große Flasche soll 13,4 cm x 6,7 cm groß sein.
In der Flasche ist ein hochwertiges natives Olivenöl.
Das Design soll frisch, klar, ansprechend, anziehend und freundlich sein.

```html
<!DOCTYPE html>
<html lang="de">
<head>
<meta charset="utf-8">
<title>Olivenöl Etikett</title>
<link href="https://fonts.googleapis.com/css2?family=Fira+Sans+Condensed:wght@300;400;600&family=Great+Vibes&family=Montserrat:wght@400;700&display=swap" rel="stylesheet">
<style>
  :root {
    --page: #ffffff;
    --label-bg: #f6f4ea;
    --leaf-tone: #ece3cf;
    --ink: #2a2a2a;
    --teal: #12393a;
    --olive: #b2b655;
    --table: #a9b04b;
    --table-line: #eef0d6;
    --heart: #ec7470;
  }
  * { margin: 0; padding: 0; box-sizing: border-box; }
  html, body { width: 1124px; height: 1200px; overflow: hidden; background: var(--page); }
  .canvas { position: relative; width: 1124px; height: 1200px; }
  .label {
    position: absolute; left: 20px; top: 329px; width: 1084px; height: 542px;
    background: var(--label-bg); overflow: hidden;
    font-family: "Fira Sans Condensed", sans-serif; color: var(--ink);
  }
  .label__pattern {
    position: absolute; inset: 0;
    background:
      radial-gradient(ellipse 260px 200px at 12% 40%, var(--leaf-tone), transparent 70%),
      radial-gradient(ellipse 240px 180px at 88% 30%, var(--leaf-tone), transparent 70%),
      radial-gradient(ellipse 220px 160px at 70% 95%, var(--leaf-tone), transparent 70%),
      radial-gradient(ellipse 200px 150px at 28% 95%, var(--leaf-tone), transparent 70%),
      var(--label-bg);
  }
  .abs { position: absolute; }
  .facts { left: 38px; top: 24px; font-weight: 300; font-size: 18px; line-height: 22px; }
  .donation { left: 38px; top: 194px; width: 170px; height: 60px; }
  .donation__heart { position: absolute; left: 44px; top: 0; width: 56px; height: 56px; }
  .donation__text {
    position: relative; font-family: "Montserrat", sans-serif; font-size: 17px; line-height: 23px;
  }
  .donation__text span { display: block; }
  .donation__text span:first-child { padding-left: 21px; }
  .pairing-title { left: 38px; top: 325px; font-weight: 600; font-size: 16px; }
  .pairing-icons { left: 38px; top: 354px; display: flex; gap: 10px; }
  .pairing-icon {
    width: 42px; height: 40px; border: 2px solid var(--ink); border-radius: 4px;
    background: linear-gradient(#e9e4d4, #ddd6c1); box-shadow: inset 0 0 0 5px var(--label-bg);
  }
  .storage { left: 38px; top: 444px; font-weight: 600; font-size: 16px; line-height: 20px; }
  .storage p + p { margin-top: 19px; }
  .brand { left: 442px; top: 34px; width: 200px; text-align: center; }
  .brand__est { font-size: 10px; font-family: "Montserrat", sans-serif; }
  .brand__name {
    margin-top: 50px; font-size: 23px; font-weight: 400; letter-spacing: 1px;
    display: inline-flex; align-items: center; gap: 8px;
  }
  .brand__dot { width: 9px; height: 9px; border-radius: 50%; background: var(--olive); }
  .title-frame { left: 358px; top: 201px; width: 367px; height: 153px; }
  .title {
    left: 358px; top: 201px; width: 367px; height: 153px;
    display: flex; align-items: center; justify-content: center;
    font-family: "Great Vibes", cursive; font-size: 86px; color: var(--teal); padding-top: 6px;
  }
  .grade { left: 392px; top: 400px; width: 300px; text-align: center; font-size: 26px; font-weight: 400; }
  .divider { left: 487px; top: 445px; width: 111px; height: 8px; }
  .harvest { left: 392px; top: 466px; width: 300px; text-align: center; font-size: 26px; font-weight: 300; }
  .producer {
    left: 818px; top: 42px; width: 240px; text-align: center; font-weight: 300;
    font-size: 18px; line-height: 22px;
  }
  .producer__mail { margin-top: 22px; }
  .nutrition {
    left: 830px; top: 334px; width: 215px; border-collapse: collapse;
    background: var(--table); color: #fff; font-size: 10.5px; font-weight: 300;
    border: 1px solid var(--table-line); border-radius: 5px; overflow: hidden;
  }
  .nutrition th { font-weight: 300; height: 24px; text-align: center; border-bottom: 1px solid var(--table-line); }
  .nutrition td { height: 17px; padding: 0 12px; border-top: 1px solid var(--table-line); }
  .nutrition td + td { border-left: 1px solid var(--table-line); text-align: center; padding: 0 4px; width: 76px; }
  .volume { right: 39px; top: 487px; font-family: "Montserrat", sans-serif; font-weight: 700; font-size: 22px; }
</style>
</head>
<body>
<main class="canvas">
  <section class="label">
    <div class="label__pattern" role="img" aria-label="Dezentes Hintergrundmuster aus Olivenzweigen und Oliven in Beige"></div>

    <div class="abs facts">
      <p>Sortenrein &amp; mühlenfrisch</p>
      <p>Kaltgepresst</p>
      <p>0,17% Ölsäure</p>
    </div>

    <div class="abs donation">
      <svg class="donation__heart" viewBox="0 0 56 56" aria-hidden="true">
        <path d="M28 52 C10 36 2 27 2 16 A13 13 0 0 1 28 11 A13 13 0 0 1 54 16 C54 27 46 36 28 52 Z" fill="var(--heart)" opacity="0.9"/>
      </svg>
      <p class="donation__text"><span>Wir Spenden</span><span>von Verkaufserlös</span></p>
    </div>

    <p class="abs pairing-title">Sorte Arbequina, ideal zu:</p>
    <div class="abs pairing-icons">
      <div class="pairing-icon" role="img" aria-label="Symbol Fisch"></div>
      <div class="pairing-icon" role="img" aria-label="Symbol Salat"></div>
      <div class="pairing-icon" role="img" aria-label="Symbol Gebäck"></div>
    </div>

    <div class="abs storage">
      <p>Mindestens haltbar bis:<br>Siehe Flasche</p>
      <p>Kühl und dunkel lagern</p>
    </div>

    <div class="abs brand">
      <p class="brand__est">Est. 2009</p>
      <p class="brand__name"><span class="brand__dot"></span>VERDANO</p>
    </div>

    <svg class="abs title-frame" viewBox="0 0 367 153" aria-hidden="true">
      <path d="M15 3 H352 A12 12 0 0 0 364 15 V138 A12 12 0 0 0 352 150 H15 A12 12 0 0 0 3 138 V15 A12 12 0 0 0 15 3 Z"
            fill="var(--label-bg)" stroke="var(--olive)" stroke-width="5"/>
    </svg>
    <h1 class="abs title">Olivenöl</h1>

    <p class="abs grade">EXTRA NATIV</p>
    <svg class="abs divider" viewBox="0 0 111 8" aria-hidden="true">
      <line x1="0" y1="4" x2="47" y2="4" stroke="var(--ink)" stroke-width="1"/>
      <circle cx="55.5" cy="4" r="3.5" fill="var(--ink)"/>
      <line x1="64" y1="4" x2="111" y2="4" stroke="var(--ink)" stroke-width="1"/>
    </svg>
    <p class="abs harvest">frühe Ernte</p>

    <div class="abs producer">
      <p>Abgefüllt von Olivares Mar<br>für Verdano OHG<br>Am Kornhof 14b<br>21073 Lindstedt<br>Deutschland</p>
      <p class="producer__mail">info@verdano-oel.de</p>
    </div>

    <table class="abs nutrition">
      <thead><tr><th colspan="2">Durchschnittliche Nährwerte pro 100 g</th></tr></thead>
      <tbody>
        <tr><td></td><td>3700 kJ / 900 kJ</td></tr>
        <tr><td>Fett</td><td>100 g</td></tr>
        <tr><td>davon gesättigte Fettsäuren</td><td>100 g</td></tr>
        <tr><td>Kohlenhydrate</td><td>0,0 g</td></tr>
        <tr><td>davon Zucker</td><td>0,0 g</td></tr>
        <tr><td>Eiweiß</td><td>0,0 g</td></tr>
        <tr><td>Salz</td><td>0,0 g</td></tr>
      </tbody>
    </table>

    <p class="abs volume">250 ml</p>
  </section>
</main>
</body>
</html>
```